Hadley & Partners, LLC Business Card 2016

We need a new business card design for a very important trade show coming up.

We are a compliance Consulting Firm. Our clients are stock brokerage firms and investment advisers.

I would like our logo on both sides of the card.

Info in the front of the card shold include:

Logo
First & Last Name
Title
Office #
Cell #
Email
Company Address (42 W. Calloway St., Suite 300 Pasadena, CA 91417

Back of the card should include the logo and url: www.hadleypartnersgroup.com

Target Market(s)

Stock Brokerage Firms and Investment Advisers

Industry/Entity Type

Financial Service

Contact Information for Business Card

Marcus J. Pellew
President
42 W. Calloway St., Suite 300
Pasadena, CA 91417
O 626.555.0147 ext. 204
C 818.555.0193
Email: marcus@hadleypartnersgroup.com
www.hadleypartnersgroup.com

Requirements
Nice to have
• The back of the card could be black with the logo with the white letters.
• I do want the front of the card to at least have the color logo with the black "Hadley & Partners Lettering.

```html
<!DOCTYPE html>
<html lang="en">
<head>
<meta charset="utf-8">
<title>Hadley &amp; Partners — Business Card</title>
<link rel="stylesheet" href="https://fonts.googleapis.com/css2?family=Cinzel:wght@400&family=Lato:wght@400;700&display=swap">
<style>
  :root {
    --backdrop: #d9d6d2;
    --card-black: #0a0a0a;
    --card-white: #ffffff;
    --brand-red: #d12a25;
    --text-dark: #2a2a2a;
    --text-grey: #5f5f5f;
    --rule-grey: #c8c8c8;
    --letter-white: #ffffff;
  }
  html, body {
    margin: 0;
    padding: 0;
    width: 1200px;
    height: 1000px;
    overflow: hidden;
    background: var(--backdrop);
  }
  .canvas {
    position: relative;
    width: 1200px;
    height: 1000px;
  }
  .card {
    position: absolute;
    left: 243px;
    width: 708px;
    box-shadow: 0 6px 18px rgba(0,0,0,0.25);
  }
  .card-back {
    top: 84px;
    height: 405px;
    background: var(--card-black);
  }
  .card-front {
    top: 527px;
    height: 403px;
    background: var(--card-white);
  }
  .wordmark {
    position: absolute;
    display: flex;
    align-items: center;
    gap: 18px;
  }
  .wordmark-square {
    width: 22px;
    height: 22px;
    background: var(--brand-red);
    flex: none;
  }
  .card-back .wordmark {
    left: 92px;
    top: 176px;
  }
  .card-back .wordmark-name {
    font-family: "Cinzel", serif;
    font-weight: 400;
    font-size: 40px;
    letter-spacing: 2px;
    color: var(--letter-white);
  }
  .card-front .wordmark {
    left: 42px;
    top: 104px;
  }
  .card-front .wordmark-name {
    font-family: "Cinzel", serif;
    font-weight: 400;
    font-size: 30px;
    letter-spacing: 1px;
    color: var(--text-dark);
  }
  .person {
    position: absolute;
    right: 39px;
    top: 202px;
    text-align: right;
    font-family: "Lato", sans-serif;
  }
  .person-name {
    font-weight: 700;
    font-size: 20px;
    color: var(--brand-red);
    line-height: 26px;
  }
  .person-title {
    font-size: 16px;
    color: var(--text-grey);
    line-height: 20px;
  }
  .divider {
    position: absolute;
    left: 40px;
    right: 39px;
    top: 259px;
    height: 1px;
    background: var(--rule-grey);
  }
  .contact-list {
    position: absolute;
    left: 40px;
    top: 271px;
    margin: 0;
    padding: 0;
    list-style: none;
    font-family: "Lato", sans-serif;
    font-size: 16px;
    color: var(--text-grey);
  }
  .contact-list li {
    display: flex;
    align-items: center;
    gap: 6px;
    height: 23px;
  }
  .contact-icon {
    width: 12px;
    height: 12px;
    flex: none;
    fill: var(--brand-red);
  }
  .address {
    position: absolute;
    right: 39px;
    top: 319px;
    text-align: right;
    font-family: "Lato", sans-serif;
    font-size: 16px;
    line-height: 21px;
    color: var(--text-grey);
  }
</style>
</head>
<body>
<main class="canvas">

  <section class="card card-back" aria-label="Card back">
    <div class="wordmark">
      <span class="wordmark-square"></span>
      <span class="wordmark-name">HADLEY &amp; PARTNERS</span>
    </div>
  </section>

  <section class="card card-front" aria-label="Card front">
    <div class="wordmark">
      <span class="wordmark-square"></span>
      <span class="wordmark-name">Hadley &amp; Partners</span>
    </div>

    <div class="person">
      <div class="person-name">Marcus J. Pellew</div>
      <div class="person-title">President</div>
    </div>

    <div class="divider"></div>

    <ul class="contact-list">
      <li>
        <svg class="contact-icon" viewBox="0 0 12 12" aria-hidden="true"><path d="M1 4c0-2 2-3 5-3s5 1 5 3l-2 1-1-2H4L3 5 1 4zM3 6h6l1 5H2l1-5z"/></svg>
        626.555.0147 ext. 204
      </li>
      <li>
        <svg class="contact-icon" viewBox="0 0 12 12" aria-hidden="true"><path d="M3.5 0h5a1 1 0 0 1 1 1v10a1 1 0 0 1-1 1h-5a1 1 0 0 1-1-1V1a1 1 0 0 1 1-1zm.5 1.5v8h4v-8H4zm2 8.6a.6.6 0 1 0 0 1.2.6.6 0 0 0 0-1.2z"/></svg>
        818.555.0193
      </li>
      <li>
        <svg class="contact-icon" viewBox="0 0 12 12" aria-hidden="true"><path d="M0 2.5h12v7H0zM0 2.5l6 4 6-4v1l-6 4-6-4z"/></svg>
        marcus@hadleypartnersgroup.com
      </li>
      <li>
        <svg class="contact-icon" viewBox="0 0 12 12" aria-hidden="true"><path d="M6 0a6 6 0 1 0 0 12A6 6 0 0 0 6 0zm0 1c.8 0 1.6 1.7 1.8 4.5H4.2C4.4 2.7 5.2 1 6 1zM1 6.5h2.2c.1 1.6.4 3 .9 3.9A5 5 0 0 1 1 6.5zm0-1a5 5 0 0 1 3.1-3.9c-.5.9-.8 2.3-.9 3.9H1zm5 5.5c-.8 0-1.6-1.7-1.8-4.5h3.6C7.6 9.3 6.8 11 6 11zm1.9-.6c.5-.9.8-2.3.9-3.9H11a5 5 0 0 1-3.1 3.9zM8.8 5.5c-.1-1.6-.4-3-.9-3.9A5 5 0 0 1 11 5.5H8.8z"/></svg>
        www.hadleypartnersgroup.com
      </li>
    </ul>

    <address class="address" style="font-style:normal">
      42 W. Calloway St., Suite 300<br>
      Pasadena, CA 91417
    </address>
  </section>

</main>
</body>
</html>
```